Ferris + Oakdale Architecture Ltd Stationary rebrand Lead designer to create a fresh clean modern...

We have recieved a great new logo design and now we are after a consistant fresh and modern stationary to match the new design. Business card design, Letter Head design, presentatnion folders and other stationery within the package. I have also added some of our existing layouts for presentation we would like updating with the new look, We would like a clean modern fresh design that looks visually pleasing on the page. we cant wait to see what you come up with!!!!

Target Market(s)

young professionals and middle age clients

Industry/Entity Type

Architect

Contact Information for Business Card

i have uploarded our orginal business card that has all the details attached.

Font styles to use
Sans Serif

Colors
000000
ffffff
d3d3d3

Requirements
Must have
• Logo and our contact information
Nice to have
• white sape around the card to give a clean look.

```html
<!DOCTYPE html>
<html lang="en">
<head>
<meta charset="utf-8">
<title>Ferris + Oakdale Architecture – Business Card</title>
<link href="https://fonts.googleapis.com/css2?family=Jost:wght@400;500&display=swap" rel="stylesheet">
<style>
  :root {
    --ink: #1b1b1b;
    --paper: #f4f4f4;
    --backdrop: #9c9c9c;
    --card-dark: #1d1d1d;
    --pattern-tone: #242424;
    --white: #ffffff;
  }
  * { margin: 0; padding: 0; box-sizing: border-box; }
  html, body { width: 1200px; height: 1017px; overflow: hidden; }
  body {
    background: var(--backdrop);
    font-family: "Jost", "Helvetica Neue", Arial, sans-serif;
    color: var(--ink);
    position: relative;
  }
  .card {
    position: absolute;
    left: 347px;
    width: 553px;
    height: 336px;
  }
  .card--front { top: 139px; background: var(--paper); }
  .card--back  { top: 548px; background: var(--card-dark); }

  .brand {
    position: absolute;
    left: 60px;
    top: 60px;
    width: 182px;
    height: 205px;
    display: flex;
    flex-direction: column;
    justify-content: flex-end;
  }
  .brand__mark {
    width: 34px; height: 34px;
    background: var(--ink);
    margin-bottom: auto;
  }
  .brand__name {
    font-weight: 500;
    font-size: 15px;
    letter-spacing: 1.6px;
    line-height: 1;
    white-space: nowrap;
  }
  .brand__sub {
    font-weight: 500;
    font-size: 8px;
    letter-spacing: 9.4px;
    margin-top: 5px;
    white-space: nowrap;
  }

  .details {
    position: absolute;
    left: 285px;
    top: 55px;
    font-size: 13.4px;
    line-height: 17px;
    letter-spacing: 0.4px;
  }
  .details__name {
    font-weight: 500;
    font-size: 17.5px;
    letter-spacing: 1.2px;
    line-height: 20px;
  }
  .details__role { margin-bottom: 16px; }
  .contact { list-style: none; margin-bottom: 16px; }
  .contact li { display: flex; align-items: center; gap: 8px; }
  .contact svg { width: 11px; height: 11px; flex: none; }
  .address { margin-bottom: 16px; }

  .back-pattern {
    position: absolute; inset: 0;
    background: linear-gradient(135deg, var(--card-dark), var(--pattern-tone));
  }
  .back-brand {
    position: absolute;
    left: 0; right: 0; top: 0; bottom: 0;
    display: flex; flex-direction: column;
    align-items: center; justify-content: center;
    color: var(--white);
  }
  .back-brand__name {
    font-weight: 500;
    font-size: 17px;
    letter-spacing: 2px;
  }
</style>
</head>
<body>
  <section class="card card--front">
    <div class="brand">
      <div class="brand__mark"></div>
      <div class="brand__name">FERRIS + OAKDALE</div>
      <div class="brand__sub">ARCHITECTURE</div>
    </div>

    <div class="details">
      <div class="details__name">MARCUS FERRIS</div>
      <div class="details__role">Director</div>
      <ul class="contact">
        <li>
          <svg viewBox="0 0 12 12"><path d="M2.5 1 L4.5 1 L5 3.5 L3.8 4.5 C4.5 6 6 7.5 7.5 8.2 L8.5 7 L11 7.5 L11 9.5 C11 10.3 10.3 11 9.5 11 C5 11 1 7 1 2.5 C1 1.7 1.7 1 2.5 1Z" fill="currentColor"/></svg>
          03 555 0142
        </li>
        <li>
          <svg viewBox="0 0 12 12"><rect x="3" y="0.8" width="6" height="10.4" rx="1" fill="none" stroke="currentColor" stroke-width="1.4"/><rect x="5" y="8.6" width="2" height="1" fill="currentColor"/></svg>
          0274 555 019
        </li>
        <li>
          <svg viewBox="0 0 12 12"><rect x="0.8" y="2.5" width="10.4" height="7" fill="currentColor"/><path d="M1 3 L6 6.5 L11 3" fill="none" stroke="#f4f4f4" stroke-width="1"/></svg>
          info@foarchitecture.co.nz
        </li>
        <li>
          <svg viewBox="0 0 12 12" fill="none" stroke="currentColor" stroke-width="0.9"><circle cx="6" cy="6" r="5"/><ellipse cx="6" cy="6" rx="2.2" ry="5"/><path d="M1 6 H11 M2 3.5 H10 M2 8.5 H10"/></svg>
          www.foarchitecture.co.nz
        </li>
      </ul>
      <div class="address">42 Harlow Street<br>Ashburton 7700</div>
      <div class="address">88 Kestrel Drive<br>Queenstown 9300</div>
    </div>
  </section>

  <section class="card card--back">
    <div class="back-pattern" role="img" aria-label="Faint repeating brand pattern in dark grey tones"></div>
    <div class="back-brand">
      <div class="back-brand__name">FERRIS + OAKDALE</div>
    </div>
  </section>
</body>
</html>
```